Business Card Design

I need a business card design for my law office based in Pasadena, California. I am a sole practitioner and I specialize in business transaction and litigation, probate and estate planning, taxation law, corporate and business formation, immigration and real estate. I want something that is simple, yet stands out.

A friend helped to create a logo about 6 years ago. I am open to new ideas to changing the logo.

Industry/Entity Type

Business

Contact Information for Business Card

Law Offices of Doran M. Vaske
482 W. Harlow Ave., Suite 312
Pasadena, CA 91108
Tel: 626-503-7719
Fax: 626-581-9046
Email: dvaske@dmvlegalgrp.example

Attorney: Doran M. Vaske

```html
<!DOCTYPE html>
<html lang="en">
<head>
<meta charset="utf-8">
<title>Law Offices of Doran M. Vaske — Business Cards</title>
<link href="https://fonts.googleapis.com/css2?family=Cinzel:wght@400&family=Open+Sans:wght@400;700&display=swap" rel="stylesheet">
<style>
  :root {
    --page-bg: #e9e7e4;
    --card-dark: #2b2b2b;
    --card-light: #ffffff;
    --ink: #111111;
    --ink-soft: #333333;
    --on-dark: #e6e6e6;
    --rule-dark: #8a8a8a;
    --rule-light: #444444;
    --shadow: rgba(0,0,0,0.18);
  }
  * { box-sizing: border-box; margin: 0; padding: 0; }
  html, body {
    width: 1200px; height: 900px; overflow: hidden;
    background: var(--page-bg);
    font-family: "Open Sans", Arial, sans-serif;
  }
  .canvas { position: relative; width: 1200px; height: 900px; }

  .card {
    position: absolute;
    width: 600px; height: 343px;
    box-shadow: 0 6px 18px var(--shadow);
    overflow: hidden;
  }

  .wordmark {
    font-family: "Cinzel", "Times New Roman", serif;
    font-weight: 400;
    text-align: center;
    white-space: nowrap;
  }
  .wordmark .eyebrow {
    display: block;
    letter-spacing: 0.55em;
    text-transform: uppercase;
  }
  .wordmark .rule { height: 1px; }
  .wordmark .name {
    display: block;
    text-transform: uppercase;
    letter-spacing: 0.02em;
    line-height: 1.1;
  }

  /* Front: dark card */
  .card--front {
    left: 420px; top: 70px;
    background: var(--card-dark);
  }
  .card--front .wordmark {
    position: absolute; left: 0; right: 0; top: 112px;
    color: var(--on-dark);
  }
  .card--front .eyebrow { font-size: 12px; margin-bottom: 6px; }
  .card--front .rule { width: 470px; margin: 0 auto 14px; background: var(--rule-dark); }
  .card--front .name { font-size: 46px; }

  /* Back: white card */
  .card--back {
    left: 180px; top: 470px;
    background: var(--card-light);
    color: var(--ink);
  }
  .card-bands { position: absolute; inset: 0; }

  .attorney {
    position: absolute; left: 82px; top: 18px;
  }
  .attorney .name { font-size: 17px; font-weight: 700; line-height: 1.2; }
  .attorney .title { font-size: 14px; color: var(--ink-soft); }

  .contact {
    position: absolute; left: 34px; top: 112px;
    font-size: 15px; line-height: 1.45;
  }
  .contact .firm { font-weight: 700; }
  .contact ul { list-style: none; margin-top: 8px; }
  .contact li { display: flex; align-items: center; gap: 10px; line-height: 1.5; }
  .contact svg { width: 12px; height: 12px; flex: none; fill: var(--ink); }

  .card--back .wordmark {
    position: absolute; left: 318px; top: 104px; width: 262px;
    color: var(--ink);
  }
  .card--back .mark {
    width: 34px; height: 34px; margin: 0 auto 10px;
    background: var(--ink);
  }
  .card--back .eyebrow { font-size: 9px; margin-bottom: 4px; }
  .card--back .rule { background: var(--rule-light); margin-bottom: 8px; }
  .card--back .name { font-size: 26px; }
</style>
</head>
<body>
<main class="canvas">

  <section class="card card--front" aria-label="Card front">
    <div class="wordmark">
      <span class="eyebrow">Law Offices of</span>
      <div class="rule"></div>
      <span class="name">Doran M. Vaske</span>
    </div>
  </section>

  <section class="card card--back" aria-label="Card back">
    <svg class="card-bands" viewBox="0 0 600 343" preserveAspectRatio="none" aria-hidden="true">
      <polygon points="14,14 62,14 34,52 14,52" fill="#111"/>
      <polygon points="0,258 250,258 238,278 0,278" fill="#111"/>
      <polygon points="262,290 600,290 600,343 232,343" fill="#111"/>
    </svg>

    <div class="attorney">
      <p class="name">Doran M. Vaske</p>
      <p class="title">Attorney</p>
    </div>

    <div class="contact">
      <p class="firm">Law Offices of Doran M. Vaske</p>
      <p>482 W. Harlow Ave., Suite 312</p>
      <p>Pasadena, CA 91108</p>
      <ul>
        <li>
          <svg viewBox="0 0 12 12" aria-label="Phone"><path d="M2.5 0.8 4.3 2.8 3.4 4.3C4 5.8 6.2 8 7.7 8.6L9.2 7.7 11.2 9.5 10.2 11.2C5.6 11 1 6.4 0.8 1.8Z"/></svg>
          626-503-7719
        </li>
        <li>
          <svg viewBox="0 0 12 12" aria-label="Fax"><rect x="3" y="0.5" width="6" height="3.5"/><rect x="0.5" y="4.5" width="11" height="5.5" rx="1"/><rect x="3" y="8.5" width="6" height="3" fill="#fff"/></svg>
          626-581-9046
        </li>
        <li>
          <svg viewBox="0 0 12 12" aria-label="Email"><rect x="0.5" y="2" width="11" height="8"/><path d="M0.8 2.3 6 6.6 11.2 2.3" fill="none" stroke="#fff" stroke-width="1"/></svg>
          dvaske@dmvlegalgrp.example
        </li>
      </ul>
    </div>

    <div class="wordmark">
      <div class="mark"></div>
      <span class="eyebrow">Law Offices of</span>
      <div class="rule"></div>
      <span class="name">Doran M. Vaske</span>
    </div>
  </section>

</main>
</body>
</html>
```